TLR Property - Business Cards

Looking for a business card & general letterhead, signage etc design for our new logo.

Colours:
000a20
0056a2
00b5ef
0088ce
68cef2

Fonts:
Poppins
Karla

Please keep look and feel of new brand - example in the zip package I sent.

```html
<!DOCTYPE html>
<html lang="en">
<head>
<meta charset="utf-8">
<title>TLR Property – Business Cards</title>
<link href="https://fonts.googleapis.com/css2?family=Poppins:wght@300;400;500;600;700;800&family=Karla:wght@400;500&display=swap" rel="stylesheet">
<style>
  :root {
    --ink: #000a20;
    --navy-card: #1b1f38;
    --navy-card-deep: #141830;
    --brand-blue: #0056a2;
    --sky: #00b5ef;
    --mid-blue: #0088ce;
    --pale-blue: #68cef2;
    --paper: #ffffff;
    --stage: #e6e8ec;
    --body-text: #2a2f3d;
  }
  * { box-sizing: border-box; margin: 0; padding: 0; }
  html, body {
    width: 1200px; height: 852px; overflow: hidden;
    background: var(--stage);
    font-family: "Poppins", sans-serif;
  }
  .sheet {
    width: 1200px; height: 852px;
    display: flex; align-items: center; justify-content: center; gap: 48px;
  }
  .card {
    position: relative;
    width: 540px; height: 309px;
    border-radius: 18px;
    overflow: hidden;
    box-shadow: 0 10px 28px rgba(0, 10, 32, 0.18);
  }

  /* Front */
  .card--front {
    background: linear-gradient(160deg, var(--navy-card) 0%, var(--navy-card-deep) 100%);
  }
  .card--front .brand {
    position: absolute; left: 160px; top: 92px;
  }
  .brand__name {
    font-weight: 800; color: var(--brand-blue);
    line-height: 0.9; letter-spacing: -1px;
  }
  .brand__sub {
    font-weight: 500; color: var(--brand-blue);
    letter-spacing: 0.42em; text-transform: uppercase;
  }
  .card--front .brand__name { font-size: 74px; }
  .card--front .brand__sub { font-size: 15px; margin-top: 4px; padding-left: 4px; }
  .front__rule {
    position: absolute; left: 0; right: 0; bottom: 22px; height: 4px;
    background: linear-gradient(90deg, var(--mid-blue), var(--sky));
  }
  .front__web {
    position: absolute; right: 28px; bottom: 38px;
    font-family: "Karla", sans-serif; font-size: 11px;
    letter-spacing: 0.5em; color: #cfd6e6;
  }

  /* Back */
  .card--back { background: var(--paper); }
  .card--back .brand { position: absolute; left: 34px; top: 34px; }
  .card--back .brand__name { font-size: 54px; }
  .card--back .brand__sub { font-size: 11px; margin-top: 3px; padding-left: 3px; }
  .person { position: absolute; left: 38px; top: 148px; }
  .person__name {
    font-size: 20px; font-weight: 600; color: var(--mid-blue); line-height: 1.1;
  }
  .person__role {
    font-size: 10.5px; font-weight: 400; color: var(--body-text); margin-top: 2px;
  }
  .contact {
    position: absolute; left: 38px; top: 204px;
    list-style: none;
    font-size: 12px; font-weight: 300; color: var(--body-text);
  }
  .contact li {
    display: flex; align-items: center; gap: 9px; height: 20px;
  }
  .contact svg { width: 12px; height: 12px; fill: var(--brand-blue); flex: none; }
  .contact .no-icon { padding-left: 21px; }
</style>
</head>
<body>
<main class="sheet">

  <section class="card card--front" aria-label="Business card front">
    <div class="brand">
      <div class="brand__name">TLR</div>
      <div class="brand__sub">Property</div>
    </div>
    <div class="front__web">www.tlrproperty.com</div>
    <div class="front__rule"></div>
  </section>

  <section class="card card--back" aria-label="Business card back">
    <div class="brand">
      <div class="brand__name">TLR</div>
      <div class="brand__sub">Property</div>
    </div>

    <div class="person">
      <div class="person__name">Daniel Hart</div>
      <div class="person__role">Managing Director</div>
    </div>

    <ul class="contact">
      <li>
        <svg viewBox="0 0 24 24" aria-hidden="true"><path d="M6.6 10.8a15.1 15.1 0 0 0 6.6 6.6l2.2-2.2c.3-.3.7-.4 1-.2 1.1.4 2.3.6 3.6.6.6 0 1 .4 1 1V20c0 .6-.4 1-1 1C10.6 21 3 13.4 3 4c0-.6.4-1 1-1h3.5c.6 0 1 .4 1 1 0 1.3.2 2.5.6 3.6.1.3 0 .7-.2 1z"/></svg>
        555-014-2290
      </li>
      <li>
        <svg viewBox="0 0 24 24" aria-hidden="true"><path d="M2 5h20v14H2z M4 7v.4l8 5 8-5V7l-8 5z" fill-rule="evenodd"/></svg>
        daniel@tlrproperty.com
      </li>
      <li>
        <svg viewBox="0 0 24 24" aria-hidden="true"><path d="M12 2a10 10 0 1 0 0 20 10 10 0 0 0 0-20zm6.9 9h-3a15 15 0 0 0-1.3-5.6A8 8 0 0 1 18.9 11zM12 4.1c.9 1.3 1.8 3.7 1.9 6.9h-3.8c.1-3.2 1-5.6 1.9-6.9zM9.4 5.4A15 15 0 0 0 8.1 11h-3a8 8 0 0 1 4.3-5.6zM5.1 13h3a15 15 0 0 0 1.3 5.6A8 8 0 0 1 5.1 13zm6.9 6.9c-.9-1.3-1.8-3.7-1.9-6.9h3.8c-.1 3.2-1 5.6-1.9 6.9zm2.6-1.3a15 15 0 0 0 1.3-5.6h3a8 8 0 0 1-4.3 5.6z"/></svg>
        www.tlrproperty.com
      </li>
      <li class="no-icon">27 Harbour View Road Northmead</li>
    </ul>
  </section>

</main>
</body>
</html>
```